Website Design for a Law Firm

We require a fully functional Website that will be added features such as live chat, Online payment system and online forms. We need to be able to edit the website and update it regularly. We have made a website structure that is attached below.

The website footer must have:
Liability limited by a Scheme approved under Professional Standards Legislation. All legal practitioners employed by Brantley Lawyers Pty Limited (including those described as Principal Solicitor) are members of the Scheme.

Target Market(s)

People seeking legal services in Australia

Industry/Entity Type

Legal

Coding

Coded - Design and coding required

Number of Pages Required

1 page

Requirements
Must have
• Online portal function where clients can upload documents; website that would work perfectly on standard mobile, tablet, laptop, and desktop sizes; the website must have an online payment system.
Nice to have
• Online portal function where clients

```html
<!DOCTYPE html>
<html lang="en">
<head>
<meta charset="utf-8">
<title>Brantley Lawyers – Legal Services in Spring Hill</title>
<link href="https://fonts.googleapis.com/css2?family=Poppins:wght@300;400;500;600;700&display=swap" rel="stylesheet">
<style>
:root{
  --teal:#1c9f8d;
  --teal-soft:#d7efeb;
  --navy:#27445a;
  --ink:#2b3a47;
  --body:#555c63;
  --grey-bg:#f3f3f3;
  --line:#d4d4d4;
  --orange:#ff8000;
  --foot:#242424;
  --foot-bar:#1b1b1b;
  --white:#fff;
}
*{box-sizing:border-box;margin:0;padding:0}
html,body{width:1200px;height:4578px;overflow:hidden}
body{font-family:'Poppins',sans-serif;color:var(--body);background:var(--white);position:relative}
.abs{position:absolute}
a{color:inherit;text-decoration:none}

/* header / hero */
.hero-photo{left:0;top:0;width:1200px;height:866px;background:linear-gradient(110deg,#8f9391 0%,#b6b8b6 35%,#9c9e9c 60%,#6f7677 100%)}
.topline{left:0;top:0;width:1200px;height:6px;background:var(--teal)}
.brand{left:75px;top:34px;font-size:36px;font-weight:500;color:var(--white);letter-spacing:1px}
.callbox{left:766px;top:0;width:360px;height:90px;background:var(--teal);color:var(--white);text-align:center;padding-top:10px}
.callbox small{display:block;font-size:18px;font-weight:400}
.callbox strong{display:block;font-size:38px;font-weight:600;line-height:1.15}
.navrule{left:0;top:111px;width:1200px;height:1px;background:rgba(255,255,255,.45)}
.nav{left:98px;top:124px;display:flex;gap:0;font-size:13.5px;font-weight:600;color:var(--white)}
.nav a{margin-right:49px;letter-spacing:.3px}
.nav a.on{color:var(--teal);position:relative}
.nav a.on:before{content:"";position:absolute;left:-16px;right:-16px;top:-14px;height:3px;background:var(--teal)}

.intro{left:0;top:711px;width:675px;height:694px;background:linear-gradient(180deg,rgba(240,240,240,.96),rgba(228,228,226,.96));padding:28px 60px 0 75px}
.intro h1{font-size:56px;font-weight:700;color:var(--navy);line-height:64px;letter-spacing:.5px}
.intro p{margin-top:24px;font-size:17px;line-height:36px;color:#4c5257}
.btn-fill{display:inline-flex;align-items:center;gap:10px;background:var(--teal);color:var(--white);font-weight:600;font-size:22px;padding:0 24px;height:64px;margin-top:40px}

.welcome{left:705px;top:982px;font-size:58px;line-height:64px;color:var(--navy);font-weight:300;letter-spacing:.5px}
.welcome b{font-weight:700}
.btn-line{display:inline-flex;align-items:center;justify-content:center;border:2px solid var(--teal);color:var(--teal);font-weight:600;font-size:22px;height:63px;background:var(--white)}

.sec-title{left:0;width:1200px;text-align:center;font-size:58px;font-weight:300;color:var(--navy);letter-spacing:.5px}
.sec-title b{font-weight:700}

/* services */
.card{width:329px;height:270px;border:1.5px solid var(--line);background:var(--white);display:flex;flex-direction:column;align-items:center;justify-content:flex-end;padding-bottom:52px;text-align:center}
.card svg{margin-bottom:26px}
.card h3{font-size:21px;font-weight:600;color:var(--ink);line-height:32px;letter-spacing:.3px}
.card.feature{background:linear-gradient(160deg,#3b5a63,#7f9293 60%,#4a6568);border:none;justify-content:center;padding:0}
.feature .frame{width:270px;height:172px;border:2px solid var(--teal);background:rgba(28,80,90,.55);display:flex;flex-direction:column;align-items:center;justify-content:center;color:var(--white)}
.feature h3{color:var(--white);font-size:21px}
.feature .more{margin-top:12px;border:2px solid var(--white);padding:10px 22px;font-size:16px;font-weight:600}

/* insights */
.insights{left:0;top:2405px;width:1200px;height:770px;background:var(--grey-bg)}
.post{width:328px;height:400px}
.post .shell{position:absolute;left:18px;top:18px;right:0;bottom:0;border:2px solid var(--teal)}
.post .body{position:absolute;left:0;top:0;right:14px;bottom:18px;background:var(--white);padding:100px 36px 0}
.post .date{position:absolute;left:0;top:0;width:212px;height:68px;background:var(--navy);color:var(--white);font-size:22px;font-weight:500;padding:24px 0 0 34px}
.post .date:after{content:"";position:absolute;right:-4px;top:16px;width:4px;height:52px;background:var(--teal)}
.post h4{font-size:22px;font-weight:600;color:var(--navy);line-height:32px}
.post p{font-size:15px;line-height:28px;margin-top:16px;color:#5b6066}
.post .read{display:inline-block;margin-top:14px;font-size:17px;font-weight:600;color:var(--teal);border-bottom:2px solid var(--teal);line-height:22px}

/* form + reviews */
.formwrap{left:67px;top:3255px;width:430px;height:670px;background:var(--teal)}
.formpanel{left:75px;top:3255px;width:422px;height:660px;background:var(--navy);padding:30px 28px 0}
.formpanel h2{font-size:43px;color:var(--white);font-weight:300;line-height:49px}
.formpanel h2 b{font-weight:700}
.field{margin-top:20px;height:56px;border:1.5px solid rgba(255,255,255,.75);color:var(--white);font-size:15px;padding:18px 14px 0;position:relative}
.field:first-of-type{margin-top:26px}
.field.msg{height:114px}
.submit{margin-top:20px;height:56px;background:var(--orange);color:var(--white);font-size:22px;font-weight:600;text-align:center;line-height:56px}

.rev-title{left:523px;top:3240px;font-size:58px;color:var(--navy);font-weight:300;line-height:64px}
.rev-title b{font-weight:700}
.review{left:523px;width:600px;display:flex;gap:22px}
.quote{flex:none;width:62px;height:62px;border-radius:50%;background:var(--teal-soft);display:flex;align-items:center;justify-content:center;margin-top:8px}
.review h5{font-size:20px;font-weight:600;color:var(--teal)}
.stars{display:flex;gap:6px;margin:4px 0 8px}
.review p{font-size:15px;line-height:28px;color:#5b6066}

/* footer */
.footer{left:0;top:4015px;width:1200px;height:495px;background:var(--foot);color:#e6e6e6}
.fcol{position:absolute;top:88px;font-size:17px;line-height:41px}
.fcol h6{font-size:21px;font-weight:600;color:var(--teal);line-height:30px;margin-bottom:4px;letter-spacing:.3px}
.hours td{padding-right:30px}
.social{display:flex;gap:22px;margin-top:14px}
.chat{left:1108px;top:4432px;width:70px;height:70px;border-radius:50%;background:#3a3a3a;display:flex;align-items:center;justify-content:center}
.copy{left:0;top:4510px;width:1200px;height:68px;background:var(--foot-bar);color:#ddd;font-size:15px;text-align:center;line-height:68px}
.copy span{color:var(--teal)}
.arrow{display:block}
</style>
</head>
<body>

<!-- hero -->
<div class="abs hero-photo" role="img" aria-label="Three lawyers in business suits posed in front of a concrete wall with a potted plant"></div>
<div class="abs topline"></div>
<div class="abs brand">Brantley Lawyers</div>
<div class="abs callbox"><small>Call 24/7 for a Free Consultation</small><strong>(07) 3000 4172</strong></div>
<div class="abs navrule"></div>
<nav class="abs nav">
  <a class="on">HOME</a><a>ABOUT US</a><a>OUR SERVICES</a><a>INSIGHTS &amp; NEWS</a><a>CAREERS</a><a>COSTS</a><a>BLOG</a><a>CONTACT US</a>
</nav>

<section class="abs intro">
  <h1>LEGAL SERVICES IN<br>SPRING HILL</h1>
  <p>Sed ut perspiciatis unde omnis iste natus error sit voluptatem accusantium doloremque laudantium, totam rem aperiam, eaque ipsa quae ab illo inventore veritatis et quasi architecto beatae vitae dicta sunt explicabo. Nemo enim ipsam voluptatem quia voluptas sit aspernatur aut odit aut fugit, sed quia consequuntur magni dolores eos qui ratione voluptatem sequi nesciunt. Neque porro quisquam est, qui dolorem ipsum quia dolor sit amet, consectetur, adipisci velit, sed quia non numquam eius modi tempora incidunt ut labore et dolore magnam aliquam quaerat voluptatem.</p>
  <a class="btn-fill"><svg width="20" height="22" viewBox="0 0 20 22"><path d="M4 2 L8 2 L9 7 L6.5 8.5 Q8 13 12 15.5 L13.5 13 L18 14 L18 18 Q16 20 13 19.5 Q4 16 2 6 Q2 3 4 2Z" fill="#fff"/></svg>Call Us Today: (07) 3000 4172</a>
</section>

<h2 class="abs welcome">WELCOME TO<br><b>BRANTLEY<br>LAWYERS</b></h2>
<a class="abs btn-line" style="left:705px;top:1210px;width:228px">More About Us</a>

<!-- services -->
<h2 class="abs sec-title" style="top:1488px">OUR <b>SERVICES</b></h2>

<div class="abs card" style="left:75px;top:1598px">
  <svg width="104" height="104" viewBox="0 0 104 104" fill="none" stroke="#1c9f8d" stroke-width="3"><rect x="22" y="8" width="58" height="82" rx="4"/><path d="M14 90 H88"/><path d="M40 40 L62 22 M48 48 L70 30 M44 44 L30 60"/><rect x="36" y="66" width="30" height="8"/></svg>
  <h3>ADMINISTRATIVE<br>LAW</h3>
</div>
<div class="abs card" style="left:437px;top:1598px">
  <svg width="104" height="104" viewBox="0 0 104 104" fill="none" stroke="#1c9f8d" stroke-width="3"><rect x="30" y="36" width="24" height="58"/><rect x="54" y="50" width="32" height="44"/><path d="M36 46h12M36 58h12M36 70h12M60 60h20M60 72h20M10 38 L36 14 M20 46 L44 22"/></svg>
  <h3>COMMERCIAL<br>LAW</h3>
</div>
<div class="abs card feature" style="left:798px;top:1598px" role="img" aria-label="Small model house on a desk">
  <div class="frame"><h3>PROPERTY<br>LAW</h3><span class="more">Read More</span></div>
</div>
<div class="abs card" style="left:75px;top:1900px">
  <svg width="104" height="104" viewBox="0 0 104 104" fill="none" stroke="#1c9f8d" stroke-width="3"><rect x="16" y="18" width="62" height="74" rx="4"/><circle cx="44" cy="50" r="18"/><path d="M26 50h36M44 32v36M78 24 L92 28 L82 86 L72 84"/></svg>
  <h3>IMMIGRATION<br>LAW</h3>
</div>
<div class="abs card" style="left:437px;top:1900px">
  <svg width="104" height="104" viewBox="0 0 104 104" fill="none" stroke="#1c9f8d" stroke-width="3"><rect x="26" y="10" width="58" height="82" rx="4"/><path d="M58 28h18M58 40h18M58 52h18"/><circle cx="32" cy="60" r="18"/><path d="M45 73 L58 86"/></svg>
  <h3>EMPLOYMENT<br>LAW</h3>
</div>
<div class="abs card" style="left:798px;top:1900px">
  <svg width="104" height="104" viewBox="0 0 104 104" fill="none" stroke="#1c9f8d" stroke-width="3"><circle cx="30" cy="30" r="12"/><circle cx="74" cy="30" r="12"/><circle cx="52" cy="52" r="9"/><path d="M10 90 V62 Q10 48 30 48 Q44 48 46 58 M94 90 V62 Q94 48 74 48 Q60 48 58 58 M38 90 V74 Q38 64 52 64 Q66 64 66 74 V90"/></svg>
  <h3>FAMILY &amp; RELATIONSHIP<br>LAW</h3>
</div>

<a class="abs btn-line" style="left:467px;top:2246px;width:266px">View All Services</a>

<!-- insights -->
<section class="abs insights"></section>
<h2 class="abs sec-title" style="top:2480px">INSIGHTS <b>&amp; NEWS</b></h2>

<svg class="abs arrow" style="left:30px;top:2766px" width="30" height="26" viewBox="0 0 30 26" fill="none" stroke="#9aa0a4" stroke-width="3"><path d="M28 13H4M14 2 3 13l11 11"/></svg>
<svg class="abs arrow" style="left:1140px;top:2766px" width="30" height="26" viewBox="0 0 30 26" fill="none" stroke="#1c9f8d" stroke-width="3"><path d="M2 13h24M16 2l11 11-11 11"/></svg>

<article class="abs post" style="left:75px;top:2588px">
  <div class="shell"></div>
  <div class="body"><h4>Complex Migration Matters - Throughout Australia</h4><p>If you have problems or concerns with the migration process or with your visa, Brantley Lawyers are here to assist you with the most relevant migration.</p><a class="read">Read More</a></div>
  <div class="date">Feb, 16, 2023</div>
</article>
<article class="abs post" style="left:437px;top:2588px">
  <div class="shell"></div>
  <div class="body"><h4>Complex Migration Matters - Throughout Australia</h4><p>If you have problems or concerns with the migration process or with your visa, Brantley Lawyers are here to assist you with the most relevant migration.</p><a class="read">Read More</a></div>
  <div class="date">Feb, 16, 2023</div>
</article>
<article class="abs post" style="left:798px;top:2588px">
  <div class="shell"></div>
  <div class="body"><h4>Complex Migration Matters - Throughout Australia</h4><p>If you have problems or concerns with the migration process or with your visa, Brantley Lawyers are here to assist you with the most relevant migration.</p><a class="read">Read More</a></div>
  <div class="date">Feb, 16, 2023</div>
</article>

<a class="abs btn-line" style="left:467px;top:3045px;width:266px;background:transparent">View All News</a>

<!-- consultation form -->
<div class="abs formwrap" style="top:3263px;left:67px;height:670px"></div>
<form class="abs formpanel">
  <h2>REQUEST <b>A FREE<br>CONSULTANT</b></h2>
  <div class="field">Full Name</div>
  <div class="field">Email Address</div>
  <div class="field">Phone No</div>
  <div class="field">Subject<svg style="position:absolute;right:10px;top:18px" width="10" height="16" viewBox="0 0 10 16" fill="#fff"><path d="M5 1 9 6H1zM5 15 1 10h8z"/></svg></div>
  <div class="field msg">Message</div>
  <div class="submit">Submit</div>
</form>

<!-- reviews -->
<h2 class="abs rev-title">OUR CLIENT<br><b>REVIEWS</b></h2>
<svg class="abs arrow" style="left:1052px;top:3294px" width="28" height="24" viewBox="0 0 30 26" fill="none" stroke="#9aa0a4" stroke-width="3"><path d="M28 13H4M14 2 3 13l11 11"/></svg>
<svg class="abs arrow" style="left:1100px;top:3294px" width="28" height="24" viewBox="0 0 30 26" fill="none" stroke="#1c9f8d" stroke-width="3"><path d="M2 13h24M16 2l11 11-11 11"/></svg>

<div class="abs review" style="top:3405px">
  <div class="quote"><svg width="30" height="24" viewBox="0 0 30 24" fill="#1c9f8d"><path d="M2 4h10v10l-5 9H3l4-9H2zM17 4h10v10l-5 9h-4l4-9h-5z"/></svg></div>
  <div><h5>Priya M</h5>
  <div class="stars"><svg width="118" height="18" viewBox="0 0 118 18" fill="#1c9f8d"><g id="st"><path d="M9 0l2.6 6 6.4.5-4.9 4.2 1.5 6.3L9 13.6 3.4 17l1.5-6.3L0 6.5 6.4 6z"/></g><use href="#st" x="25"/><use href="#st" x="50"/><use href="#st" x="75"/><use href="#st" x="100"/></svg></div>
  <p>“ Many thanks for the friendly, competent and effective cooperation. Thanks to the good preparation of my visa applications were processed quickly and successfully. I always feel very well advised and supported. I can really recommend the Brantley Lawyers with a clear conscience..”</p></div>
</div>
<div class="abs review" style="top:3633px">
  <div class="quote"><svg width="30" height="24" viewBox="0 0 30 24" fill="#1c9f8d"><path d="M2 4h10v10l-5 9H3l4-9H2zM17 4h10v10l-5 9h-4l4-9h-5z"/></svg></div>
  <div><h5>Priya M</h5>
  <div class="stars"><svg width="118" height="18" viewBox="0 0 118 18" fill="#1c9f8d"><use href="#st"/><use href="#st" x="25"/><use href="#st" x="50"/><use href="#st" x="75"/><use href="#st" x="100"/></svg></div>
  <p>“ Many thanks for the friendly, competent and effective cooperation. Thanks to the good preparation of my visa applications were processed quickly and successfully. I always feel very well advised and supported. I can really recommend the Brantley Lawyers with a clear conscience..”</p></div>
</div>
<a class="abs btn-line" style="left:523px;top:3860px;width:266px">View All Reviews</a>

<!-- footer -->
<footer class="abs footer">
  <div class="fcol" style="left:75px"><h6>SITE MAP</h6>Home<br>About Us<br>Our Services<br>Insights &amp; News<br>Careers<br>Costs<br>Blog<br>Contact Us</div>
  <div class="fcol" style="left:303px"><h6>SERVICES</h6>Administrative Law<br>Commercial Law<br>Property Law<br>Immigration Law<br>Employment Law<br>Family &amp; Relationship Law<br>Criminal<br>Professional Misconduct</div>
  <div class="fcol" style="left:603px;line-height:32px"><h6 style="margin-bottom:10px">CONTACT INFO</h6>Level 2/48 Ashgrove<br>Street Spring Hill QLD 4000<br>Australia<br><span style="display:block;margin-top:4px">(07) 3000 4172</span><span style="display:block;margin-top:4px">hello@brantleylaw.example</span>
    <div class="social">
      <svg width="18" height="18" viewBox="0 0 18 18" fill="#bbb"><rect x="1" y="1" width="16" height="16" rx="3"/></svg>
      <svg width="18" height="18" viewBox="0 0 18 18" fill="#bbb"><circle cx="9" cy="9" r="8"/></svg>
      <svg width="18" height="18" viewBox="0 0 18 18" fill="#bbb"><rect x="1" y="1" width="16" height="16" rx="3"/></svg>
      <svg width="18" height="18" viewBox="0 0 18 18" fill="#bbb"><circle cx="9" cy="9" r="8"/></svg>
      <svg width="18" height="18" viewBox="0 0 18 18" fill="#bbb"><rect x="1" y="1" width="16" height="16" rx="3"/></svg>
    </div>
  </div>
  <div class="fcol" style="left:916px"><h6>HOURS</h6>
    <table class="hours" style="border-collapse:collapse;font-size:17px;line-height:36px;color:#e6e6e6">
      <tr><td>Mon:</td><td>8:30AM – 5:00PM</td></tr><tr><td>Tue:</td><td>8:30AM – 5:00PM</td></tr><tr><td>Wed:</td><td>8:30AM – 5:00PM</td></tr><tr><td>Thu:</td><td>8:30AM – 5:00PM</td></tr><tr><td>Fri:</td><td>8:30AM – 5:00PM</td></tr><tr><td>Sat:</td><td>Closed</td></tr><tr><td>Sun:</td><td>Closed</td></tr>
    </table>
  </div>
</footer>
<div class="abs chat"><svg width="40" height="32" viewBox="0 0 40 32" fill="#fff"><path d="M4 2h32v20H16l-8 8v-8H4z"/><circle cx="14" cy="12" r="2" fill="#3a3a3a"/><circle cx="20" cy="12" r="2" fill="#3a3a3a"/><circle cx="26" cy="12" r="2" fill="#3a3a3a"/></svg></div>
<div class="abs copy">Copyright © 2023. Brantley Lawyers.All Right Reserved. <span>Compliance &amp; Disclaimers</span></div>

</body>
</html>
```